Web Design + logo Project

hi,
we are based in ASEAN region (Malaysia/Indonesia/Singapore), involving in Online Vehicle Insurance Portal. so far our product is only car insurance and personal insurance, and motorbikes insurance)
We need a webdesign + logo for KotaLindung.com
The website is www.kotalindung.example. The website is already up with the necessary quotation comparison + purchase mechanism.
We like www.vantorelo.example look and feel very much.
Blue is the preferred main theme.
The mainpage should highlight the following
1) quotation generator/input
2) hotline number
3) news/testimonial
The webdesign should be able to cater for mobile users as well.
The design should be professional and energetic
Target Market(s)
20-35years old vehicle owners in Indonesia/thailand/Singapore/vietnam
Industry/Entity Type
Car Insurance
Look and feel
Each slider illustrates characteristics of the customer's brand and the style your logo design should communicate.

```html
<!DOCTYPE html>
<html lang="en">
<head>
<meta charset="utf-8">
<title>KotaLindung – Online Vehicle Insurance</title>
<link href="https://fonts.googleapis.com/css2?family=PT+Sans:wght@400;700&family=PT+Sans+Narrow:wght@400;700&display=swap" rel="stylesheet">
<style>
:root{
  --blue:#1a8fd0;
  --blue-dark:#0a6eb4;
  --blue-deep:#0d4f86;
  --blue-light:#2aa6e6;
  --text:#222;
  --muted:#555;
  --line:#c9c9c9;
  --tile:#f1f2f3;
  --white:#fff;
}
*{margin:0;padding:0;box-sizing:border-box}
html,body{width:1114px;height:1200px;overflow:hidden;background:var(--white)}
body{font-family:"PT Sans",sans-serif;color:var(--text);position:relative}
.abs{position:absolute}

/* header */
.brand{left:147px;top:13px;display:flex;align-items:center;gap:12px}
.brand-mark{width:54px;height:54px;border-radius:50%;background:var(--blue)}
.brand-name{font-weight:700;font-size:31px;color:var(--blue)}
.live-chat{left:651px;top:27px;width:127px;height:26px;background:linear-gradient(#1ea0e6,#0b77c2);border-radius:3px;color:var(--white);font-size:14px;line-height:26px;padding-left:54px}
.live-chat .agent{position:absolute;left:4px;top:-10px;width:44px;height:44px;border-radius:50%;background:linear-gradient(#d8c3b2,#8c7a6c);border:2px solid var(--white)}
.hotline{left:801px;top:30px;display:flex;align-items:center;gap:6px;font-size:13px;color:var(--muted)}
.hotline strong{font-weight:400;font-size:17px;color:var(--blue)}

/* nav */
.main-nav{left:147px;top:81px;width:821px;height:23px;background:linear-gradient(#1ea3ea,#0a72bc);border-radius:3px;display:flex;font-size:12px;color:var(--white)}
.main-nav a{color:inherit;text-decoration:none;padding:0 16px;line-height:23px;border-right:1px solid rgba(255,255,255,.35)}
.main-nav .search{margin-left:auto;width:171px;background:var(--blue-deep);padding-left:12px;line-height:23px;position:relative;border-radius:0 3px 3px 0}
.main-nav .search svg{position:absolute;right:6px;top:4px}

/* hero */
.hero{left:147px;top:109px;width:821px;height:404px;background:linear-gradient(160deg,#c9d6e6 0%,#9fb3cc 45%,#6e86a6 100%);box-shadow:0 8px 10px -6px rgba(0,0,0,.35)}
.hero-caption{left:696px;top:287px;width:272px;height:107px;background:rgba(235,240,246,.75);padding:14px 20px;color:var(--blue-deep);font-size:19px;line-height:22px}
.hero-caption p+p{margin-top:12px}
.helper{left:60px;top:189px;width:112px;height:282px;background:linear-gradient(#c7a48c,#9c9c9c);border-radius:50px 40px 10px 10px}

.quote-box{left:149px;top:141px;width:226px;height:229px;background:linear-gradient(#1a95dc,#0b73bd);color:var(--white);border-radius:3px 3px 0 0}
.quote-box > *{position:absolute;left:28px;right:12px;white-space:nowrap}
.quote-box h2{top:10px;font-weight:400;font-size:17px;line-height:22px}
.select{height:21px;background:var(--white);color:var(--blue);font-size:11px;line-height:21px;padding-left:8px}
.select::after{content:"";position:absolute;right:3px;top:3px;width:14px;height:14px;background:var(--blue-dark)}
.select::before{content:"";position:absolute;right:7px;top:8px;border:3px solid transparent;border-top:4px solid var(--white);z-index:1}
.field-label{font-size:11px;line-height:14px}
.radios{display:flex;gap:12px;font-size:10.5px;line-height:14px}
.radios span::before{content:"";display:inline-block;width:9px;height:9px;border-radius:50%;background:#dfe6ec;margin-right:5px;vertical-align:-1px}
.radios.divided{padding-bottom:8px;border-bottom:1px solid rgba(255,255,255,.3)}
.btn{display:inline-block;background:linear-gradient(#1b8fd6,#0b5ea2);color:var(--white);font-size:11px;padding:3px 9px;border-radius:3px;border:1px solid rgba(255,255,255,.4);white-space:nowrap}
.quote-box .quote-btn{left:auto;right:12px;top:202px}

.login{left:149px;top:370px;width:226px;height:116px;background:var(--white);padding:6px 13px 0 30px;box-shadow:0 1px 3px rgba(0,0,0,.25)}
.login h3{font-weight:400;font-size:15px;line-height:20px;margin-bottom:4px}
.input{height:23px;border:1px solid #bbb;font-size:10px;line-height:21px;padding-left:8px;margin-bottom:6px}
.login-foot{display:flex;align-items:center;font-size:10px;gap:5px;white-space:nowrap}
.login-foot > *{flex-shrink:0}
.login-foot .sep{width:1px;height:12px;background:#bbb}
.login-foot .btn{padding:2px 8px}
.dots{left:551px;top:517px;display:flex;gap:4px}
.dots i{width:8px;height:8px;border-radius:50%;background:#ccc}
.dots i.on{background:var(--blue-deep)}

/* service tiles */
.tile{top:542px;width:199px;height:47px;background:linear-gradient(#fafafa,#e9eaeb);border-radius:3px;box-shadow:0 2px 3px rgba(0,0,0,.15);display:flex;align-items:center}
.tile .ico{width:50px;flex-shrink:0;height:100%;display:flex;align-items:center;justify-content:center;border-right:1px solid #d5d5d5}
.tile span{font-family:"PT Sans Narrow",sans-serif;font-size:18px;color:var(--blue-deep);padding-left:14px;white-space:nowrap}

.dotted{left:150px;width:820px;border-top:1px dotted #999}

/* intro */
.intro-title{left:147px;top:640px;font-family:"PT Sans Narrow",sans-serif;font-size:20px}
.intro-title b{color:var(--blue);font-weight:400;font-size:22px;margin-left:8px}
.intro-text{left:147px;top:674px;width:824px;font-size:11px;line-height:19px}
.bullets{font-size:14px;color:var(--blue)}
.bullets li{list-style:none;height:26px;padding-left:26px;position:relative;white-space:nowrap}
.bullets li::before{content:"";position:absolute;left:0;top:3px;width:11px;height:11px;border-radius:50%;background:#ececec;border:1px solid #ccc}
.bullets li::after{content:"";position:absolute;left:5px;top:6px;border:3px solid transparent;border-left:3px solid #777}
.bullets.dark{color:var(--text);font-size:13.5px}

/* news */
.news-label{left:152px;top:810px;font-family:"PT Sans Narrow",sans-serif;font-size:19px;color:var(--blue);display:flex;align-items:center;gap:10px}
.news-bar{left:278px;top:807px;width:692px;height:24px;background:linear-gradient(#1ea3ea,#0a72bc);border-radius:2px;display:flex;font-size:10.5px;color:var(--white);white-space:nowrap;overflow:hidden}
.news-bar span{padding:0 14px 0 26px;line-height:24px;position:relative;border-right:1px solid rgba(255,255,255,.35)}
.news-bar span::before{content:"";position:absolute;left:10px;top:9px;border:3px solid transparent;border-left:4px solid var(--white)}

.renew-title{left:153px;top:870px;font-family:"PT Sans Narrow",sans-serif;font-size:18px;color:var(--blue)}
.newsletter{left:637px;top:865px;width:333px;height:111px;background:linear-gradient(#1da2e8,#0b78c4);padding:14px 16px;color:var(--white)}
.newsletter h4{font-family:"PT Sans Narrow",sans-serif;font-weight:400;font-size:17px;margin-bottom:7px}
.newsletter .email{height:25px;background:var(--white);border:1px solid #0b6aa8;color:var(--blue);font-size:10px;line-height:23px;padding-left:7px}
.newsletter .btn{position:absolute;right:14px;top:78px;background:linear-gradient(#1c6fb8,#0b3f75)}

/* footer */
.footer{left:150px;top:992px;width:820px;height:203px;background:linear-gradient(#ededed,#fbfbfb);border:1px solid #ddd}
.social{position:absolute;top:21px;left:277px;display:flex}
.social div{width:62px;text-align:center;font-size:9px;color:var(--muted);white-space:nowrap}
.social i{display:block;width:36px;height:36px;margin:0 auto 8px;border-radius:4px;background:var(--blue)}
.foot-line{position:absolute;left:42px;top:93px;width:736px;border-top:1px solid #bbb}
.foot-links{position:absolute;width:100%;text-align:center;font-size:9.5px;color:#444;white-space:nowrap}
.foot-links a{color:inherit;text-decoration:none;padding:0 5px}
.copyright{position:absolute;left:319px;top:164px;width:179px;height:20px;background:#b0b0b0;font-size:9.5px;text-align:center;line-height:20px;color:#222;white-space:nowrap}
</style>
</head>
<body>

<header>
  <div class="abs brand"><span class="brand-mark"></span><span class="brand-name">KotaLindung</span></div>
  <div class="abs live-chat"><span class="agent" role="img" aria-label="Photo of support agent with headset"></span>LIVE CHAT</div>
  <div class="abs hotline">
    <svg width="14" height="18" viewBox="0 0 14 18"><path d="M3 1c2 0 3 3 2 5l-1 1c1 3 2 5 4 6l1-1c2-1 5 0 5 2l-1 3c-6 0-12-7-12-14z" fill="#999"/></svg>
    Call Us <strong>415.XXX.XXXX</strong>
  </div>
  <nav class="abs main-nav">
    <a>Home</a><a>About Us</a><a>Motor Insurance</a><a>Personal Insurance</a><a>Customer Service</a><a>Contact Us</a>
    <span class="search">Search
      <svg width="16" height="15" viewBox="0 0 16 15"><rect width="16" height="15" rx="2" fill="#2aa6e6"/><circle cx="7" cy="6.5" r="3.5" fill="none" stroke="#fff" stroke-width="1.6"/><path d="M9.5 9l3 3" stroke="#fff" stroke-width="1.8"/></svg>
    </span>
  </nav>
</header>

<section>
  <div class="abs hero" role="img" aria-label="Photo of two young women riding a scooter, one pointing ahead, under a bright sky"></div>
  <div class="abs hero-caption"><p>You love riding on your two wheeler, anywhere, anytime.</p><p>Trust us to keep you secure</p></div>
  <div class="abs helper" role="img" aria-label="Photo of a smiling man peeking from behind the quote panel"></div>
  <form class="abs quote-box">
    <h2>GET A FREE QUOTE</h2>
    <div class="select" style="top:35px">Type of Vehicle</div>
    <div class="select" style="top:64px">Year</div>
    <div class="select" style="top:93px">Price Assured</div>
    <div class="field-label" style="top:127px">CATEGORY</div>
    <div class="radios divided" style="top:143px"><span>Personal</span><span style="margin-left:10px">Service</span></div>
    <div class="field-label" style="top:170px">COVERAGE</div>
    <div class="radios" style="top:186px"><span>Total Loss Only</span><span>Comprehensive</span></div>
    <span class="btn quote-btn">Get a Quote</span>
  </form>
  <form class="abs login">
    <h3>Login</h3>
    <div class="input">User Name</div>
    <div class="input">Password</div>
    <div class="login-foot"><span>New User</span><span class="sep"></span><span>Forgot Password?</span><span class="btn">LOGIN</span></div>
  </form>
  <div class="abs dots"><i></i><i></i><i class="on"></i><i></i><i></i></div>
</section>

<section>
  <div class="abs tile" style="left:147px"><div class="ico"><svg width="26" height="24" viewBox="0 0 26 24"><path d="M4 11l3-8h12l3 8v8H4z" fill="#0a6eb4"/><rect x="8" y="5" width="10" height="5" fill="#fff"/><circle cx="8" cy="15" r="2" fill="#fff"/><circle cx="18" cy="15" r="2" fill="#fff"/><rect x="4" y="19" width="4" height="4" fill="#0a6eb4"/><rect x="18" y="19" width="4" height="4" fill="#0a6eb4"/></svg></div><span>Motor Insurance</span></div>
  <div class="abs tile" style="left:354px"><div class="ico"><svg width="28" height="24" viewBox="0 0 28 24"><circle cx="6" cy="18" r="4" fill="none" stroke="#0a6eb4" stroke-width="2"/><circle cx="22" cy="18" r="4" fill="none" stroke="#0a6eb4" stroke-width="2"/><path d="M6 18l6-8h6l4 8M14 10l2-6h4" fill="none" stroke="#0a6eb4" stroke-width="2.5"/></svg></div><span style="padding-left:10px">Motorbike Insurance</span></div>
  <div class="abs tile" style="left:561px"><div class="ico"><svg width="24" height="22" viewBox="0 0 24 22"><rect x="1" y="4" width="22" height="17" rx="2" fill="#fff" stroke="#999"/><rect x="8" y="1" width="8" height="4" fill="none" stroke="#999"/><path d="M10 8h4v3h3v4h-3v3h-4v-3H7v-4h3z" fill="#d0202a"/></svg></div><span>Health Insurance</span></div>
  <div class="abs tile" style="left:770px"><div class="ico"><svg width="22" height="22" viewBox="0 0 22 22"><rect x="2" y="4" width="15" height="15" fill="none" stroke="#0a6eb4" stroke-width="2"/><path d="M9 13l9-9 2 2-9 9H9z" fill="#0a6eb4"/></svg></div><span>Claims Center</span></div>

  <div class="abs dotted" style="top:620px"></div>
  <h1 class="abs intro-title" style="font-weight:400">Buy Online Vehicle Insurance from <b>KOTALINDUNG</b></h1>
  <p class="abs intro-text">Your vehicle insurance is about freedom and the Perisaku vehicle insurance policy has been designed to set you free. Our comprehensive vehicleinsurance policy provides hassle-free protection to your bike or scooter against physical damage, theft and third party liability.</p>
  <ul class="abs bullets" style="left:176px;top:724px"><li>Cashless settlement in preferred workshops</li><li>Hassle-free claim settlement</li></ul>
  <ul class="abs bullets" style="left:521px;top:724px"><li>Quick and easy steps to purchase online</li><li>24x7 claim support</li></ul>

  <div class="abs dotted" style="top:791px"></div>
  <div class="abs news-label">LATEST NEWS <svg width="22" height="10" viewBox="0 0 22 10"><path d="M0 5h20M16 1l4 4-4 4" fill="none" stroke="#555" stroke-width="1.3"/></svg></div>
  <div class="abs news-bar"><span>Insure yours cards against loss or misuse</span><span>Know your Policy Before Buying Health Insurance</span><span>Insure yours cards against loss or misuse</span></div>
  <div class="abs dotted" style="top:853px"></div>

  <h2 class="abs renew-title" style="font-weight:400">WANT TO RENEW YOUR VEHICLE INSURANCE?</h2>
  <ul class="abs bullets dark" style="left:154px;top:905px"><li>Extra protection through 8 add on covers</li><li>7 days claims settlement service</li></ul>
  <ul class="abs bullets dark" style="left:446px;top:907px"><li>Free Car Pick Up</li><li>Warranty on Repairs</li></ul>

  <form class="abs newsletter">
    <h4>NEWSLETTER SIGNUP</h4>
    <div class="email">Enter the E mail id</div>
    <span class="btn">Sign Up</span>
  </form>
</section>

<footer class="abs footer">
  <div class="social">
    <div><i></i>View Blog</div>
    <div><i></i>Follow us</div>
    <div><i></i>Connect</div>
    <div><i></i>View &amp; Share</div>
  </div>
  <div class="foot-line"></div>
  <div class="foot-links" style="top:108px"><a>Home</a>| <a>About Us</a>| <a>Motor Insurance</a>| <a>Travel Insurance</a>| <a>Customer Service</a>| <a>Contact Us</a></div>
  <div class="foot-links" style="top:132px"><a>Terms &amp; Conditions</a>| <a>Privacy Policy</a></div>
  <div class="copyright">Copyrights @ 2012 All Rights Reserved</div>
</footer>

</body>
</html>
```